MOLVT Study flyer

I need help designing a flyer for a research study that will include brain imaging in adolescents. The info is in the attached document. The study is called the Marrowby Orchard Lantern Vesper Trail (MOLVT) study. Ideally this would be returned as a document that I can edit in the future as we will have several new recruitment phases (different age groups, etc. I also would love to have a logo designed as part of this project, but I recognize that might be a separate design request.

```html
<!DOCTYPE html>
<html lang="en">
<head>
<meta charset="utf-8">
<title>MOLVT Study Flyer</title>
<link rel="stylesheet" href="https://fonts.googleapis.com/css2?family=Saira+Condensed:ital,wght@0,700;0,800;1,800&family=Outfit:wght@400;500&display=swap">
<style>
:root{
  --teal:#00806f;
  --white:#ffffff;
  --ink:#1c1c1c;
  --backdrop:#c6c6c6;
  --scan-dark:#1d2a44;
  --scan-light:#8a9bbf;
  --head:"Saira Condensed", Impact, sans-serif;
  --body:"Outfit", Arial, sans-serif;
}
*{margin:0;padding:0;box-sizing:border-box}
html,body{width:906px;height:1200px;overflow:hidden;background:var(--backdrop)}
.flyer{position:absolute;left:73px;top:30px;width:760px;height:1140px;background:var(--white);overflow:hidden;font-family:var(--body);color:var(--ink)}
.hero{position:absolute;left:0;top:0;width:760px;height:358px;background:var(--teal)}
.hero-photo{position:absolute;left:0;top:0;width:330px;height:358px;
  background:linear-gradient(135deg,var(--scan-light) 0%,var(--scan-dark) 45%,#3c4d72 70%,var(--scan-dark) 100%);
  clip-path:polygon(0 0,329px 0,276px 358px,0 358px)}
.hero-text{position:absolute;left:300px;width:460px;top:0;text-align:center;color:var(--white)}
.study-name{position:absolute;left:0;right:0;top:60px;font-family:var(--head);font-weight:800;font-size:24px;line-height:22px;letter-spacing:.6px;text-transform:uppercase}
.headline{position:absolute;left:0;right:0;top:128px;font-family:var(--head);font-weight:800;font-size:35px;line-height:31px;letter-spacing:.3px;text-transform:uppercase}
.intro{position:absolute;left:36px;right:30px;top:232px;font-size:13px;line-height:19px}
.panel{position:absolute;left:44px;width:672px;border:2px solid var(--teal);border-radius:24px}
.panel-involves{top:399px;height:288px}
.panel-eligible{top:718px;height:255px}
.tab{position:absolute;height:50px;background:var(--teal);color:var(--white);border-radius:8px;font-family:var(--head);font-weight:800;font-size:28px;line-height:50px;text-align:center;letter-spacing:1px;text-transform:uppercase}
.tab-involves{left:175px;width:409px;top:383px}
.tab-eligible{left:130px;width:501px;top:701px}
.steps{position:absolute;left:135px;top:458px;width:565px;list-style:none;font-size:21px;line-height:25px}
.steps li{position:relative;margin-bottom:21px}
.steps li::before{content:"";position:absolute;left:-28px;top:6px;width:11px;height:11px;border-radius:50%;background:var(--teal)}
.criterion{position:absolute;top:776px;width:220px;text-align:center;font-size:16px;line-height:20px}
.criterion-icon{display:block;width:108px;height:108px;margin:0 auto 16px;border-radius:50%;background:var(--teal)}
.crit-age{left:14px}
.crit-worry{left:226px}
.crit-diagnosis{left:491px;width:200px}
.contact{position:absolute;left:0;top:993px;width:760px;height:147px;background:var(--teal)}
.contact-call{position:absolute;left:0;right:0;top:12px;text-align:center;color:var(--white);font-family:var(--head);font-style:italic;font-weight:800;font-size:31px;line-height:29px;letter-spacing:.3px;text-transform:uppercase}
.email{position:absolute;left:72px;top:92px;display:flex;align-items:center;gap:12px;color:var(--white);font-size:24px}
.email-icon{width:36px;height:36px;border-radius:50%;background:var(--white);display:flex;align-items:center;justify-content:center}
.compensation{position:absolute;left:478px;top:78px;width:282px;height:69px;background:var(--white);border-top-left-radius:22px;color:var(--teal);font-family:var(--head);font-weight:800;font-size:33px;line-height:29px;letter-spacing:.5px;text-align:center;padding-top:6px;text-transform:uppercase}
</style>
</head>
<body>
<main class="flyer">
  <section class="hero">
    <div class="hero-photo" role="img" aria-label="Photo of a clinician's hand pointing at a wall of brain MRI scans"></div>
    <div class="hero-text">
      <p class="study-name">Marrowby Orchard Lantern<br>Vesper Trail</p>
      <h1 class="headline">Are you the parent of a child<br>age 10-17? Do they worry or<br>overthink negative emotions?</h1>
      <p class="intro">Halvorsen University researchers are seeking girls age 10-17 for a study about brain activity in emotions and decision-making and how they relate to puberty, anxiety and depression.</p>
    </div>
  </section>

  <div class="panel panel-involves"></div>
  <h2 class="tab tab-involves">Study participation involves</h2>
  <ul class="steps">
    <li>One one-hour interview (online or in-person) where your child will discuss their thoughts</li>
    <li>Online questionnaires (parent and child)</li>
    <li>One two-hour visit where your child will complete an MRI scan, answer questions about their puberty stage, and have a small hair sample taken to study puberty hormones</li>
  </ul>

  <div class="panel panel-eligible"></div>
  <h2 class="tab tab-eligible">Your child may be eligible if they</h2>
  <div class="criterion crit-age">
    <span class="criterion-icon" role="img" aria-label="Age icon"></span>
    Are age 10-17
  </div>
  <div class="criterion crit-worry">
    <span class="criterion-icon" role="img" aria-label="Icon of a head in profile with question marks"></span>
    Tend to worry or overthink negative thoughts
  </div>
  <div class="criterion crit-diagnosis">
    <span class="criterion-icon" role="img" aria-label="Icon of a child surrounded by puzzle pieces"></span>
    Have not been diagnosed with psychosis, learning problems, or autism
  </div>

  <section class="contact">
    <p class="contact-call">Interested in participating?<br>Want more information? Please contact us!</p>
    <div class="email">
      <span class="email-icon">
        <svg width="18" height="13" viewBox="0 0 18 13" aria-hidden="true"><rect x="1" y="1" width="16" height="11" fill="none" stroke="var(--teal)" stroke-width="1.5"/><path d="M1 1 l8 6 8-6" fill="none" stroke="var(--teal)" stroke-width="1.5"/></svg>
      </span>
      molvtstudy@halvorsen.edu
    </div>
    <div class="compensation">Compensation<br>up to $140</div>
  </section>
</main>
</body>
</html>
```